Look Round Eastvale....a heavily based video and picture gallery style website.

Would like a multipage website for videos and pictures. For example, one page/category will be Events. I would like that page to be a thumbnail gallery where the user would click on a thumbnail and the video will play over/hover the the thumbnail page(not go to another page). So when the user closes the player, they are still on the events page. On each page, would like a navigation bar to be able to go to the other pages/categories. And I would like it this way for the other categories as well (people, places, meet the vendors, pictures....) Please view my current website for all pages needed. I only submitted a fraction of images. How should i send the videos? Please contact if questions.
My current website is at www.lookroundeastvale.net

Target Market(s)

male/female, 30-70+ years old

Industry/Entity Type

Entertainment

Coding

Coded - Design and coding required

Number of Pages Required

5+ page

Font styles to use
Sans Serif

Colors
0393ce
00a990
f04a51
f68d4e

Requirements
Must have
• social media links. the video player must play/hover over the current page rather than going to another page. my logo. a calendar page where I can add events to it. a text area under videos for description, photo gallery for each category, the ability to copy a page to use as a template to add more videos and pictures in the future, contact page, the ability to add google ads, affiliate advertising.

```html
<!DOCTYPE html>
<html lang="en">
<head>
<meta charset="utf-8">
<title>Look Round Eastvale</title>
<link href="https://fonts.googleapis.com/css2?family=Roboto:wght@300;400;500;700&display=swap" rel="stylesheet">
<style>
:root{
  --blue:#0393ce;
  --blue-dark:#0279ab;
  --text:#555;
  --muted:#777;
  --light:#f4f4f4;
  --footer:#2b2b2b;
  --footer-bottom:#1f1f1f;
  --footer-text:#bbb;
  --white:#fff;
}
*{box-sizing:border-box;margin:0;padding:0}
html,body{width:1200px;height:2406px;overflow:hidden}
body{font-family:'Roboto',sans-serif;color:var(--text);background:var(--white);position:relative}
.abs{position:absolute}

/* hero */
.hero{left:0;top:0;width:1200px;height:618px;background:linear-gradient(180deg,#5d6876 0%,#3f4a50 30%,#4b4a32 55%,#3a3b30 75%,#2c2f2e 100%)}
.follow{left:160px;top:32px;display:flex;align-items:center;gap:6px;color:var(--white);font-size:12px;font-weight:700;letter-spacing:.5px}
.follow span{margin-right:6px}
.dot{width:19px;height:19px;border-radius:50%;background:var(--white);display:inline-block}
.brand{left:480px;top:0;width:240px;height:80px;background:var(--white);clip-path:polygon(0 0,100% 0,84% 100%,16% 100%);display:flex;align-items:center;justify-content:center;gap:6px;font-weight:700;font-size:15px;color:#1c3d5a}
.brand-sq{width:10px;height:10px;background:#1c3d5a}
.search{left:797px;top:24px;width:241px;height:32px;border:1px solid rgba(255,255,255,.8);display:flex}
.search span{flex:1;color:#eee;font-size:9px;letter-spacing:.5px;padding:11px 10px}
.search i{width:32px;border-left:1px solid rgba(255,255,255,.8);display:flex;align-items:center;justify-content:center}
.nav{left:160px;top:104px;width:878px;height:37px;border-top:1px solid rgba(255,255,255,.7);border-bottom:1px solid rgba(255,255,255,.7);display:flex;justify-content:center}
.nav a{color:var(--white);font-size:10px;text-decoration:none;padding:0 14px;display:flex;align-items:center;letter-spacing:.3px}
.nav a.active{background:var(--blue)}
.hero-title{left:0;top:238px;width:1200px;text-align:center;color:var(--white);font-size:36px;font-weight:500;letter-spacing:2px}
.hero-play{left:578px;top:346px}
.slide-arrow{top:273px;width:53px;height:53px;background:var(--blue);display:flex;align-items:center;justify-content:center}

/* sections */
.section-title{left:0;width:1200px;text-align:center;color:var(--blue);font-size:19px;letter-spacing:1px;font-weight:400}
.section-title::after{content:"";display:block;width:46px;height:3px;border-radius:0 0 50% 50%;background:var(--blue);margin:6px auto 0}
.row{left:0;width:1200px;height:180px}
.card{position:absolute;width:202px;top:0}
.card.fade{opacity:.35}
.thumb{width:202px;height:131px;position:relative;border-bottom:4px solid #ddd}
.thumb .play{position:absolute;left:79px;top:43px;width:46px;height:46px;background:rgba(40,40,40,.7);display:flex;align-items:center;justify-content:center}
.card p{text-align:center;font-size:10px;letter-spacing:.6px;color:var(--text);margin-top:13px;text-transform:uppercase;line-height:1.4}
.pager{display:flex;gap:8px;left:566px}
.pager i{width:29px;height:29px;background:var(--blue);display:flex;align-items:center;justify-content:center}

.g1{background:linear-gradient(135deg,#9fb0a6,#c88a9a 40%,#3a3a3a 75%,#7b8f9c)}
.g2{background:linear-gradient(180deg,#a9b7c3 0%,#b8c4c9 55%,#5e7a3d 60%,#6f8a44 100%)}
.g3{background:linear-gradient(135deg,#3c0f24,#9c2a5c 50%,#2a0c1a)}
.g4{background:linear-gradient(135deg,#c6601b,#e2b14c 40%,#b23a1c 70%,#7a8a4a)}
.g5{background:linear-gradient(135deg,#c8c8c0,#8c9098 60%,#5a5e52)}
.g6{background:linear-gradient(180deg,#4a5a3c,#7a6a4c 50%,#d8c8a8)}

/* feature */
.feature-img{left:160px;top:1585px;width:427px;height:244px;background:linear-gradient(135deg,#2a0a18,#a82a62 45%,#4a1030 80%,#1a0810)}
.feature-go{left:536px;top:1778px;width:51px;height:51px;background:var(--blue);display:flex;align-items:center;justify-content:center}
.feature-title{left:160px;top:1842px;color:var(--blue);font-size:17px;letter-spacing:.6px;font-weight:400}
.feature-text{left:160px;top:1876px;width:420px;font-size:11px;line-height:19px;color:var(--muted)}
.story{left:610px;width:430px;height:100px}
.story .s-img{position:absolute;left:0;top:0;width:128px;height:83px}
.story .s-go{position:absolute;left:106px;top:61px;width:22px;height:22px;background:var(--blue);display:flex;align-items:center;justify-content:center}
.story h3{position:absolute;left:145px;top:0;font-size:12px;color:var(--blue);font-weight:400;letter-spacing:.4px;text-transform:uppercase}
.story p{position:absolute;left:145px;top:25px;width:285px;font-size:10.5px;line-height:17px;color:var(--muted)}

/* contact strip */
.footer{left:0;top:1994px;width:1200px;height:340px;background:var(--footer)}
.strip{left:160px;top:1957px;width:877px;height:80px;background:var(--blue);display:flex;color:var(--white)}
.strip div{flex:1;display:flex;align-items:center;gap:18px;padding-left:40px;font-size:10.5px;line-height:15px}
.strip div+div{border-left:1px solid rgba(255,255,255,.35)}
.strip svg{flex:none}

.fcol{top:2072px;width:210px}
.fcol h4{color:var(--blue);font-size:12px;font-weight:500;letter-spacing:.3px}
.fcol h4::after{content:"";display:block;width:30px;height:2px;background:var(--blue);margin-top:4px}
.fbrand{margin-top:34px;font-size:14px;font-weight:700;color:#d0d0d0;display:flex;align-items:center;gap:6px}
.fbrand i{width:9px;height:9px;background:#d0d0d0;display:inline-block}
.fcol p{font-size:10.5px;line-height:17px;color:var(--footer-text)}
.services{display:grid;grid-template-columns:112px 112px;row-gap:10px;margin-top:28px}
.services span{font-size:10.5px;color:var(--footer-text);display:flex;align-items:center;gap:8px}
.services span::before{content:"";width:9px;height:9px;border-radius:50%;background:#bbb;flex:none}
.ev{display:flex;gap:14px;align-items:flex-start;margin-top:0;height:47px}
.ev b{width:50px;height:40px;flex:none;border:2px solid #ddd;background:linear-gradient(135deg,#7a2a40,#c07a4a)}
.ev span{font-size:10.5px;color:var(--footer-text);line-height:14px;text-transform:uppercase}
.newsbox{margin-top:20px;width:201px;height:34px;border:1px solid #bbb;display:flex}
.newsbox span{flex:1;font-size:10px;color:#ccc;padding:11px 8px}
.newsbox i{width:32px;border-left:1px solid #bbb;display:flex;align-items:center;justify-content:center}
.fsocial{display:flex;gap:6px;margin-top:14px}
.fsocial i{width:26px;height:26px;border-radius:50%;background:#8a8a8a;display:inline-block}
.bottom{left:0;top:2334px;width:1200px;height:72px;background:var(--footer-bottom);color:#aaa;font-size:9.5px;text-align:center;line-height:72px;letter-spacing:.3px}
</style>
</head>
<body>

<header class="abs hero" role="img" aria-label="Photo of a rocky river winding through autumn trees below forested mountains"></header>
<div class="abs follow"><span>FOLLOW US ON</span><i class="dot"></i><i class="dot"></i><i class="dot"></i><i class="dot"></i></div>
<div class="abs brand"><i class="brand-sq"></i>Look Round Eastvale</div>
<div class="abs search"><span>ENTER YOUR SEARCH</span><i><svg width="12" height="12" viewBox="0 0 12 12"><circle cx="5" cy="5" r="3.6" fill="none" stroke="#fff" stroke-width="1.6"/><path d="M7.6 7.6l3 3" stroke="#fff" stroke-width="1.8"/></svg></i></div>
<nav class="abs nav">
  <a class="active" href="#">HOME</a><a href="#">VIDEOS ▾</a><a href="#">PHOTO GALLERY ▾</a><a href="#">CALENDAR</a><a href="#">CONTACT</a>
</nav>
<h1 class="abs hero-title">WELCOME TO LOOK ROUND EASTVALE</h1>
<svg class="abs hero-play" width="44" height="56" viewBox="0 0 44 56"><path d="M3 3l38 25L3 53z" fill="none" stroke="#fff" stroke-width="3.5" stroke-linejoin="round"/></svg>
<div class="abs slide-arrow" style="left:0"><svg width="18" height="16" viewBox="0 0 18 16"><path d="M17 8H3M9 2L3 8l6 6" fill="none" stroke="#fff" stroke-width="3"/></svg></div>
<div class="abs slide-arrow" style="left:1147px"><svg width="18" height="16" viewBox="0 0 18 16"><path d="M1 8h14M9 2l6 6-6 6" fill="none" stroke="#fff" stroke-width="3"/></svg></div>

<!-- recent uploads -->
<h2 class="abs section-title" style="top:658px">RECENT UPLOADS</h2>
<section class="abs row" style="top:730px">
  <div class="card fade" style="left:-64px"><div class="thumb g5" role="img" aria-label="Market stall video still"><span class="play"><svg width="18" height="22"><path d="M2 2l14 9-14 9z" fill="none" stroke="#fff" stroke-width="2"/></svg></span></div><p>Root Farm</p></div>
  <div class="card" style="left:160px"><div class="thumb g1" role="img" aria-label="Video still of guests posing outdoors"><span class="play"><svg width="18" height="22"><path d="M2 2l14 9-14 9z" fill="none" stroke="#fff" stroke-width="2"/></svg></span></div><p>Guest Photo Montage</p></div>
  <div class="card" style="left:387px"><div class="thumb g2" role="img" aria-label="Video still of a kite over a grassy field"><span class="play"><svg width="18" height="22"><path d="M2 2l14 9-14 9z" fill="none" stroke="#fff" stroke-width="2"/></svg></span></div><p>Navruz 2017</p></div>
  <div class="card" style="left:611px"><div class="thumb g3" role="img" aria-label="Video still of musicians on a dim stage"><span class="play"><svg width="18" height="22"><path d="M2 2l14 9-14 9z" fill="none" stroke="#fff" stroke-width="2"/></svg></span></div><p>Elm Street Gallery</p></div>
  <div class="card" style="left:836px"><div class="thumb g4" role="img" aria-label="Video still of a colourful painted artwork"><span class="play"><svg width="18" height="22"><path d="M2 2l14 9-14 9z" fill="none" stroke="#fff" stroke-width="2"/></svg></span></div><p>Glen's Berries</p></div>
  <div class="card fade" style="left:1057px"><div class="thumb g5" role="img" aria-label="Event tent video still"><span class="play"><svg width="18" height="22"><path d="M2 2l14 9-14 9z" fill="none" stroke="#fff" stroke-width="2"/></svg></span></div><p>Marco &amp; Danny</p></div>
</section>
<div class="abs pager" style="top:909px"><i><svg width="10" height="10"><path d="M7 1L3 5l4 4" fill="none" stroke="#fff" stroke-width="2"/></svg></i><i><svg width="10" height="10"><path d="M3 1l4 4-4 4" fill="none" stroke="#fff" stroke-width="2"/></svg></i></div>

<!-- coming soon -->
<h2 class="abs section-title" style="top:972px">COMING SOON</h2>
<section class="abs row" style="top:1043px">
  <div class="card fade" style="left:-64px"><div class="thumb g5" role="img" aria-label="Market stall video still"><span class="play"><svg width="18" height="22"><path d="M2 2l14 9-14 9z" fill="none" stroke="#fff" stroke-width="2"/></svg></span></div><p>Camel Kitchen</p></div>
  <div class="card" style="left:160px"><div class="thumb g1" role="img" aria-label="Video still of guests posing outdoors"><span class="play"><svg width="18" height="22"><path d="M2 2l14 9-14 9z" fill="none" stroke="#fff" stroke-width="2"/></svg></span></div><p>Through My Lens Photography</p></div>
  <div class="card" style="left:387px"><div class="thumb g2" role="img" aria-label="Video still of a kite over a grassy field"><span class="play"><svg width="18" height="22"><path d="M2 2l14 9-14 9z" fill="none" stroke="#fff" stroke-width="2"/></svg></span></div><p>Hat Parade</p></div>
  <div class="card" style="left:611px"><div class="thumb g3" role="img" aria-label="Video still of musicians on a dim stage"><span class="play"><svg width="18" height="22"><path d="M2 2l14 9-14 9z" fill="none" stroke="#fff" stroke-width="2"/></svg></span></div><p>Hank's Smokehouse</p></div>
  <div class="card" style="left:836px"><div class="thumb g4" role="img" aria-label="Video still of a colourful painted artwork"><span class="play"><svg width="18" height="22"><path d="M2 2l14 9-14 9z" fill="none" stroke="#fff" stroke-width="2"/></svg></span></div><p>Rosa's Fresh Salsa</p></div>
  <div class="card fade" style="left:1057px"><div class="thumb g5" role="img" aria-label="Event tent video still"><span class="play"><svg width="18" height="22"><path d="M2 2l14 9-14 9z" fill="none" stroke="#fff" stroke-width="2"/></svg></span></div><p>Pop Corner</p></div>
</section>
<div class="abs pager" style="top:1222px"><i><svg width="10" height="10"><path d="M7 1L3 5l4 4" fill="none" stroke="#fff" stroke-width="2"/></svg></i><i><svg width="10" height="10"><path d="M3 1l4 4-4 4" fill="none" stroke="#fff" stroke-width="2"/></svg></i></div>

<!-- events -->
<h2 class="abs section-title" style="top:1286px">OUR EVENTS</h2>
<section class="abs row" style="top:1359px">
  <div class="card" style="left:160px"><div class="thumb g6" role="img" aria-label="Photo of dancers performing on an outdoor stage"></div><p>Ethnicfest 2017</p></div>
  <div class="card" style="left:387px"><div class="thumb g2" role="img" aria-label="Photo of a kite flying over a field"></div><p>Kite Festival</p></div>
  <div class="card" style="left:611px"><div class="thumb g1" role="img" aria-label="Photo of guests in costume at a park"></div><p>Alice in Wonderland at<br>Harbor Lawn Park</p></div>
  <div class="card" style="left:836px"><div class="thumb g4" role="img" aria-label="Photo of a colourful painted artwork"></div><p>Rosa's Fresh Salsa</p></div>
</section>

<!-- featured -->
<div class="abs feature-img" role="img" aria-label="Photo of a keyboard player and drummer performing under red stage light"></div>
<div class="abs feature-go"><svg width="20" height="20" viewBox="0 0 20 20"><circle cx="10" cy="10" r="9" fill="#fff"/><path d="M5 10h8M10 6l4 4-4 4" fill="none" stroke="#0393ce" stroke-width="2.2"/></svg></div>
<h3 class="abs feature-title">MARCO BELLINI AND DANNY HOLLIS</h3>
<p class="abs feature-text">The Honky-Tonk Rebel Marco Bellini and legendary drummer Danny Hollis perform for us in Millbrook. They also gave us an interview before the show.</p>

<article class="abs story" style="top:1585px">
  <div class="s-img" style="background:linear-gradient(180deg,#eee,#c9c0b8)" role="img" aria-label="Photo of a model on a fashion runway"></div>
  <span class="s-go"><svg width="12" height="12" viewBox="0 0 12 12"><circle cx="6" cy="6" r="5.5" fill="#fff"/><path d="M3 6h5M6 3.6L8.4 6 6 8.4" fill="none" stroke="#0393ce" stroke-width="1.5"/></svg></span>
  <h3>The Saffira Spring Fling Fashion Show</h3>
  <p>We experienced a little fashion at the Brookline Mall hosted by Saffira Fashion. Showcasing other local designers as well.</p>
</article>
<article class="abs story" style="top:1699px">
  <div class="s-img" style="background:linear-gradient(180deg,#e8ecef,#8c949a)" role="img" aria-label="Photo of an event hall sign"></div>
  <span class="s-go"><svg width="12" height="12" viewBox="0 0 12 12"><circle cx="6" cy="6" r="5.5" fill="#fff"/><path d="M3 6h5M6 3.6L8.4 6 6 8.4" fill="none" stroke="#0393ce" stroke-width="1.5"/></svg></span>
  <h3>Clam Jam 2017</h3>
  <p>There was lots of fun to be had at the 2017 Clam Jam. There was food, entertainment, vendors, oyster competitions and of course, the chance to pick as many oysters and clams as you wish.</p>
</article>
<article class="abs story" style="top:1813px">
  <div class="s-img" style="background:linear-gradient(135deg,#6a6a60,#2e3a44)" role="img" aria-label="Photo of an herbalist during an interview"></div>
  <span class="s-go"><svg width="12" height="12" viewBox="0 0 12 12"><circle cx="6" cy="6" r="5.5" fill="#fff"/><path d="M3 6h5M6 3.6L8.4 6 6 8.4" fill="none" stroke="#0393ce" stroke-width="1.5"/></svg></span>
  <h3>Willow - Riverside Herbalist</h3>
  <p>We visited Willow as she talks about her journey in becoming an herbalist. She also talks about what she does as an herbalist and the importance of using herbs as a supplement for overall health.</p>
</article>

<!-- footer -->
<footer class="abs footer"></footer>
<div class="abs strip">
  <div><svg width="30" height="30" viewBox="0 0 30 30"><circle cx="15" cy="15" r="14" fill="none" stroke="#fff" stroke-width="1.5"/><path d="M15 22s-5-5.5-5-9a5 5 0 0110 0c0 3.5-5 9-5 9z" fill="#fff"/><circle cx="15" cy="13" r="1.8" fill="#0393ce"/></svg><span>Donec fermentum eleifend erat, at<br>blandit ipsum commodo at.</span></div>
  <div><svg width="30" height="30" viewBox="0 0 30 30"><circle cx="15" cy="15" r="14" fill="none" stroke="#fff" stroke-width="1.5"/><path d="M11 9l3 3-1.6 1.8a9 9 0 004.8 4.8L19 17l3 3-2 2c-5 0-11-6-11-11z" fill="#fff"/></svg><span>(+01) 555-010-2233<br>(+01) 555-010-4466</span></div>
  <div><svg width="30" height="30" viewBox="0 0 30 30"><circle cx="15" cy="15" r="14" fill="none" stroke="#fff" stroke-width="1.5"/><rect x="9" y="11" width="12" height="9" fill="#fff"/><path d="M9 11l6 5 6-5" fill="none" stroke="#0393ce" stroke-width="1.2"/></svg><span>info@lookroundeastvale.net<br>support@lookroundeastvale.net</span></div>
</div>

<div class="abs fcol" style="left:160px">
  <h4>ABOUT US</h4>
  <div class="fbrand"><i></i>Look Round Eastvale</div>
  <p style="margin-top:34px;width:200px">Lorem ipsum dolor sit amet, consectetur adipiscing elit. Maecenas orci leo, consectetur molestie neque a, venenatis aliquam dolor. Nullam et hendrerit ex. Duis neque purus</p>
</div>
<div class="abs fcol" style="left:387px;width:230px">
  <h4>SERVICES</h4>
  <div class="services">
    <span>People</span><span>Eastvale Peeps</span>
    <span>Events</span><span>Places</span>
    <span>Meet the Vendors</span><span>Meet the Events</span>
    <span>Scenic Video</span><span>Roses &amp; Flowers</span>
    <span>Performance</span><span>Performance</span>
    <span>Lighter Side</span><span>Scenery</span>
    <span>Quote of the day</span><span>Water Activity</span>
  </div>
</div>
<div class="abs fcol" style="left:610px">
  <h4>EVENTS</h4>
  <div style="margin-top:20px">
    <div class="ev"><b role="img" aria-label="Concert thumbnail"></b><span>Marco Bellini and<br>Danny Hollis</span></div>
    <div class="ev"><b role="img" aria-label="Fashion show thumbnail"></b><span>The Saffira Spring Fling<br>Fashion Show</span></div>
    <div class="ev"><b role="img" aria-label="Festival thumbnail"></b><span>Clam Jam 2017</span></div>
    <div class="ev"><b role="img" aria-label="Artist thumbnail"></b><span>Lena Marquez -<br>Needle Painter</span></div>
  </div>
</div>
<div class="abs fcol" style="left:836px">
  <h4>NEWSLETTER</h4>
  <p style="margin-top:22px">Lorem ipsum dolor sit amet, consectetur adipiscing elit. Maecenas orci leo,</p>
  <div class="newsbox"><span>Enter your email address</span><i><svg width="12" height="10"><path d="M1 5h9M6 1l4 4-4 4" fill="none" stroke="#ddd" stroke-width="1.6"/></svg></i></div>
  <h4 style="margin-top:22px">FOLLOW US ON</h4>
  <div class="fsocial"><i></i><i></i><i></i><i></i></div>
</div>

<div class="abs bottom">© 2008-2017 LOOK ROUND EASTVALE. ALL RIGHT RESERVED</div>

</body>
</html>
```